Verpackungen für neue online Schokoladenmarke
Zielgruppe
Eine neue online Schokoladenmarke deren Zielgruppe sind anspruchsvolle Schokoladenliebhaber,
denn die Schokolade wird aus Kakaobohnen langzeitgewalzt.
Die Käufer essen nicht süß, sondern wünschen den wirklichen Kakaobohnengeschmack ohne
Zusatzstoffe.
Die Schokolade wird nur online verkauft.
Aufgabenstellung
Markenname: nib4tab Chocolate ---------- oder----- NIB4TAB Chocolate oder ?
Der Markenname soll dominant sein, und die Vorderseite eines Tafelkartons prägen, als
Umverpackung 80 x 160 mm - die Vorderseite, nur die ist hier beauftragt.
Obwohl Bio, muss die Verpackung nicht recycelt oder 'alternativ' aussehen, nicht im Öko - Design auftreten.
Bitte keine angebissenen Schokotafeln, Sahnetöpfe oder sonstige altmodischen Grafiken nutzen.
Der Firmenname nib4tab soll (gut lesbar) gestaltet werden, in Groß- oder Kleinbuchstaben etc. Eventuell
einen Bezug auf Online haben, oder auch nicht...
Der Gewinner kann ggf. weitere Designaufträge und auch die Layouts bzw. Datenübergabe für den
Kartonhersteller machen. Dauerbetreuung erwünscht..!

```html
<!DOCTYPE html>
<html lang="en">
<head>
<meta charset="utf-8">
<title>nib4tab Chocolate – bar carton front</title>
<link rel="stylesheet" href="https://fonts.googleapis.com/css2?family=Allura&family=Montserrat:wght@500&display=swap">
<style>
  :root {
    --slate: #343535;
    --gold: #e9b325;
    --gold-light: #fbcb38;
    --gold-deep: #c99400;
    --ink: #3a3a3a;
  }
  html, body {
    margin: 0;
    padding: 0;
    overflow: hidden;
    background: var(--slate);
  }
  .carton-front {
    position: relative;
    width: 1200px;
    height: 2400px;
    overflow: hidden;
    background: var(--slate);
  }
  .paisley-border {
    position: absolute;
    top: 0;
    right: 0;
    width: 552px;
    height: 2400px;
    background:
      radial-gradient(ellipse 60% 18% at 60% 12%, rgba(251,203,56,0.38), rgba(251,203,56,0) 70%),
      radial-gradient(ellipse 55% 16% at 45% 36%, rgba(251,203,56,0.34), rgba(251,203,56,0) 70%),
      radial-gradient(ellipse 60% 18% at 55% 62%, rgba(251,203,56,0.34), rgba(251,203,56,0) 70%),
      radial-gradient(ellipse 65% 20% at 65% 88%, rgba(251,203,56,0.4), rgba(251,203,56,0) 70%),
      linear-gradient(90deg, rgba(233,179,37,0.08), rgba(233,179,37,0.22));
  }
  .script {
    position: absolute;
    margin: 0;
    font-family: "Allura", cursive;
    font-weight: 400;
    color: var(--gold);
    text-shadow: 4px 8px 10px rgba(0,0,0,0.35);
    line-height: 1;
    white-space: nowrap;
  }
  .category {
    left: 64px;
    top: 860px;
    font-size: 190px;
    transform: rotate(-20deg);
    transform-origin: left bottom;
  }
  .claim-pure {
    left: 165px;
    top: 1800px;
    font-size: 200px;
  }
  .claim-desire {
    left: 140px;
    top: 2010px;
    font-size: 200px;
  }
  .brand-ribbon {
    position: absolute;
    left: 0;
    top: 0;
    width: 1200px;
    height: 2400px;
    filter: drop-shadow(0 14px 14px rgba(0,0,0,0.45));
  }
  .brand-name {
    font-family: "Montserrat", sans-serif;
    font-weight: 500;
    font-size: 225px;
    letter-spacing: 6px;
    fill: var(--ink);
  }
</style>
</head>
<body>
<main class="carton-front">
  <div class="paisley-border" role="img" aria-label="Gold filigree paisley ornament running down the right side"></div>

  <p class="script category">chocolate</p>

  <svg class="brand-ribbon" viewBox="0 0 1200 2400" xmlns="http://www.w3.org/2000/svg">
    <defs>
      <linearGradient id="ribbonGold" x1="0" y1="0" x2="0" y2="1">
        <stop offset="0" stop-color="#c99400"/>
        <stop offset="0.3" stop-color="#fbcb38"/>
        <stop offset="0.65" stop-color="#c99400"/>
        <stop offset="1" stop-color="#fbcb38"/>
      </linearGradient>
    </defs>
    <path d="M0 1098 C60 1125 130 1130 230 1100 C520 1010 820 920 1060 912 C1130 910 1180 920 1200 925
             L1200 1330 C1160 1290 1110 1275 1050 1280 C760 1300 480 1370 200 1440 C110 1465 40 1485 0 1470 Z"
          fill="url(#ribbonGold)"/>
    <text class="brand-name" x="170" y="1330" transform="rotate(-10 600 1250)">nib4tab</text>
  </svg>

  <p class="script claim-pure">Pure</p>
  <p class="script claim-desire">Desire</p>
</main>
</body>
</html>
```